Mental Health care Company in Washington DC

We are a new mental health care services provider in Washington DC. Please look at these sites.
https://marlowbrookpartners.com
https://www.quillstoneinc.com
https://velmarsh-kt.org/
https://www.trivanqx.com
https://www.thelanternofqz.com

```html
<!DOCTYPE html>
<html lang="en">
<head>
<meta charset="utf-8">
<title>Calder Health Services — Mental Wellness Care</title>
<link href="https://fonts.googleapis.com/css2?family=Poppins:wght@400;500;600;700&display=swap" rel="stylesheet">
<style>
:root{
  --cyan:#8bd9e3;
  --cyan-soft:#bfeaf0;
  --cyan-accent:#7fdde6;
  --teal:#2bb2bf;
  --orange:#f58220;
  --orange-deep:#f47a1c;
  --ink:#1b1b1b;
  --text:#333;
  --navy:#0c1842;
  --white:#fff;
  --card-border:#f5b98a;
}
*{box-sizing:border-box;margin:0;padding:0}
html,body{width:1200px;height:3373px;overflow:hidden}
body{font-family:"Poppins",sans-serif;color:var(--ink);background:var(--white);position:relative}
.abs{position:absolute}
a{color:inherit;text-decoration:none}

/* shared */
.arrow-dot{display:inline-flex;align-items:center;justify-content:center;width:26px;height:26px;border-radius:50%;background:var(--orange);color:#fff;flex:none}
.arrow-dot.light{background:#fff;color:var(--orange)}
.arrow-dot svg{width:12px;height:12px}
.btn{position:absolute;display:flex;align-items:center;justify-content:space-between;border-radius:16px;font-size:11.5px;font-weight:500;padding:0 4px 0 18px}
.btn-orange{background:var(--orange);color:#fff}
.btn-outline{border:1.5px solid var(--orange);color:var(--ink);background:transparent}
.btn-white{background:#fff;color:var(--ink)}
.nav-arrow{position:absolute;width:28px;height:28px;border-radius:50%;border:1.5px solid var(--orange);display:flex;align-items:center;justify-content:center;color:var(--orange);background:rgba(255,255,255,.5)}
.nav-arrow svg{width:12px;height:12px}
.section-title{position:absolute;left:0;width:1200px;display:flex;justify-content:center;align-items:center;gap:12px;font-size:39px;font-weight:600;line-height:1}
.section-title::before,.section-title::after{content:"";width:96px;height:2px;background:var(--orange)}

/* header */
.site-header{left:0;top:0;width:1200px;height:54px;background:var(--cyan)}
.logo{position:absolute;display:flex;flex-direction:column;align-items:center;color:#fff}
.logo .name{font-size:25px;font-weight:500;line-height:1;letter-spacing:-.5px}
.logo .tag{font-size:7.5px;letter-spacing:5px;margin-top:2px}
.main-nav{position:absolute;top:0;height:54px;font-size:11.5px;font-weight:500;color:var(--ink)}
.main-nav a{position:absolute;top:19px}
.main-nav a.active{color:var(--orange);border-bottom:1.5px solid var(--orange);padding-bottom:2px}
.header-cta{position:absolute;left:913px;top:14px;width:164px;height:27px;border-radius:14px;background:var(--orange);color:#fff;font-size:11.5px;font-weight:500;display:flex;align-items:center;justify-content:center}

/* hero */
.hero{left:0;top:54px;width:1200px;height:583px;background:linear-gradient(90deg,#e4e2df 0%,#dcd9d5 45%,#c9c4bd 70%,#b7b0a6 100%)}
.hero-photo{position:absolute;left:560px;top:0;width:640px;height:583px;background:radial-gradient(ellipse at 60% 45%,#efece7 0%,#d6d1ca 55%,rgba(200,195,188,0) 80%)}
.hero h1{position:absolute;left:122px;top:170px;font-size:48px;font-weight:600;line-height:54px;color:var(--ink)}
.hero h1 .hl{color:var(--cyan-accent)}
.hero h1 .rule{display:inline-block;width:124px;height:2px;background:var(--orange);vertical-align:middle;margin-left:14px}
.hero p{position:absolute;left:122px;top:285px;width:420px;font-size:11.5px;line-height:17px;color:var(--text)}

/* about */
.about-visual{left:122px;top:703px;width:558px;height:387px}
.about-text{left:688px;top:785px;width:396px}
.about-text h2{font-size:39px;font-weight:600;display:flex;align-items:center;gap:12px;line-height:1}
.about-text h2::after{content:"";width:104px;height:2px;background:var(--orange)}
.about-text p{font-size:11.3px;line-height:17.5px;color:var(--text);margin-top:16px}
.about-text p+p{margin-top:17px}

/* services */
.services{left:0;top:1150px;width:1200px;height:486px;background:linear-gradient(180deg,#8fd9e4 0%,#a9e2ea 50%,#8ed6e1 100%)}
.service-card{position:absolute;top:135px;width:225px;height:224px;background:#fff;border-radius:12px;overflow:hidden}
.service-card .photo{height:170px}
.service-card .foot{display:flex;align-items:center;justify-content:space-between;padding:0 12px 0 18px;height:54px}
.service-card h3{font-size:15px;font-weight:600;line-height:17px}

/* why */
.why-card{position:absolute;top:1771px;width:305px;height:124px;border:1.5px solid var(--card-border);border-radius:12px;background:#fff;display:flex;align-items:center;gap:16px;padding-left:26px}
.why-card .icon{width:70px;height:70px;border-radius:50%;background:var(--teal);box-shadow:0 0 0 4px #d6f0f3;display:flex;align-items:center;justify-content:center;flex:none}
.why-card .icon svg{width:36px;height:36px}
.why-card h3{font-size:15px;font-weight:600;line-height:18px}

/* testimonials */
.testimonials{left:0;top:1958px;width:1200px;height:375px;background:linear-gradient(180deg,#86e6ee 0%,#bdf0f4 35%,#eafafb 65%,#cdeef5 100%)}
.review{position:absolute;top:2094px;width:400px}
.review .avatar{position:absolute;left:0;top:0;width:78px;height:78px;border-radius:50%;background:linear-gradient(160deg,#c9a78e,#6c4e3f);border:3px solid var(--teal)}
.review .who{position:absolute;left:96px;top:16px;font-size:14.5px;color:var(--text)}
.review .stars{position:absolute;left:96px;top:40px;display:flex;gap:4px}
.review .stars svg{width:18px;height:18px}
.review blockquote{position:absolute;left:0;top:98px;width:400px;font-size:15.5px;line-height:23px;color:var(--ink)}
.review-divider{left:580px;top:2100px;width:1px;height:170px;background:#9aa}

/* blog */
.post-card{position:absolute;top:2481px;width:306px;height:258px;border-radius:14px;overflow:hidden}
.post-card .caption{position:absolute;left:0;bottom:0;width:100%;height:110px;background:linear-gradient(180deg,rgba(0,0,0,0),rgba(0,0,0,.55));display:flex;align-items:flex-end;justify-content:space-between;padding:0 14px 12px 24px;color:#fff}
.post-card h3{font-size:15px;font-weight:500;line-height:18px}

/* cta */
.cta{left:0;top:2800px;width:1200px;height:250px;background:linear-gradient(90deg,#f89a2b 0%,#f58a22 50%,#f47a1c 100%)}
.cta h2{position:absolute;left:0;width:1200px;top:52px;display:flex;justify-content:center;align-items:center;gap:8px;font-size:39px;font-weight:500;color:#fff;line-height:1}
.cta h2::before,.cta h2::after{content:"";width:96px;height:2px;background:#fff}
.cta p{position:absolute;left:350px;top:102px;width:500px;text-align:center;font-size:10.5px;line-height:14px;color:#fff}

/* footer */
.site-footer{left:0;top:3050px;width:1200px;height:323px;background:var(--navy);color:#fff}
.site-footer h4{position:absolute;font-size:15px;font-weight:500}
.foot-links a,.foot-contact div{position:absolute;font-size:11.5px}
.social{position:absolute;width:26px;height:26px;border-radius:50%;border:1.5px solid var(--orange);display:flex;align-items:center;justify-content:center}
.social span{width:8px;height:8px;border-radius:50%;background:var(--orange)}
.contact-ico{display:inline-flex;width:24px;height:24px;border-radius:50%;border:1.5px solid var(--orange);align-items:center;justify-content:center;margin-right:6px;vertical-align:middle}
.contact-ico svg{width:12px;height:12px}
.email-field{position:absolute;left:865px;top:100px;width:212px;height:31px;border:1.5px solid #fff;border-radius:16px;font-size:10.5px;padding:9px 12px}
.subscribe{position:absolute;left:865px;top:139px;width:212px;height:32px;border-radius:16px;background:var(--orange);font-size:11px;font-weight:500;display:flex;align-items:center;justify-content:center}
.foot-rule{position:absolute;left:122px;top:252px;width:956px;height:1px;background:#5a6488}
.copyright{position:absolute;left:122px;top:261px;font-size:10px}
.legal{position:absolute;right:122px;top:261px;font-size:10px;display:flex;gap:14px}
</style>
</head>
<body>

<svg width="0" height="0" style="position:absolute">
  <defs>
    <symbol id="chev-r" viewBox="0 0 12 12"><path d="M4 2l4 4-4 4" fill="none" stroke="currentColor" stroke-width="2" stroke-linecap="round" stroke-linejoin="round"/></symbol>
    <symbol id="chev-l" viewBox="0 0 12 12"><path d="M8 2L4 6l4 4" fill="none" stroke="currentColor" stroke-width="2" stroke-linecap="round" stroke-linejoin="round"/></symbol>
    <symbol id="star" viewBox="0 0 20 20"><path d="M10 1.5l2.6 5.4 5.9.8-4.3 4.1 1 5.9L10 14.9l-5.2 2.8 1-5.9L1.5 7.7l5.9-.8z" fill="#f7c81e"/></symbol>
  </defs>
</svg>

<!-- Header -->
<header class="abs site-header">
  <div class="logo" style="left:122px;top:11px"><span class="name">Calder Health</span><span class="tag">SERVICES</span></div>
  <nav class="main-nav" style="left:0;width:1200px">
    <a class="active" style="left:568px">Home</a>
    <a style="left:631px">About Us</a>
    <a style="left:711px">Services</a>
    <a style="left:787px">Blog</a>
    <a style="left:841px">Contact</a>
  </nav>
  <a class="header-cta">Make an Appointment</a>
</header>

<!-- Hero -->
<section class="abs hero">
  <div class="hero-photo" role="img" aria-label="Smiling woman in a white shirt holding a tablet in a bright living room"></div>
  <h1>Your <span class="hl">Mental</span> Wellness<br>Starts Here<span class="rule"></span></h1>
  <p>Compassionate, evidence-based care for your mind, body, and spirit — because healing is possible.</p>
  <a class="btn btn-orange" style="left:122px;top:346px;width:182px;height:32px">Book an Appointment <span class="arrow-dot light"><svg><use href="#chev-r"/></svg></span></a>
  <a class="btn btn-outline" style="left:310px;top:346px;width:169px;height:32px">Explore Our Services <span class="arrow-dot"><svg><use href="#chev-r"/></svg></span></a>
</section>

<!-- About -->
<svg class="abs about-visual" viewBox="0 0 558 387" role="img" aria-label="Group therapy session with people seated on sofas, shown inside a plus-shaped frame">
  <defs>
    <linearGradient id="aboutFill" x1="0" y1="0" x2="1" y2="0">
      <stop offset="0" stop-color="#b58466"/><stop offset=".45" stop-color="#8a8a7a"/><stop offset="1" stop-color="#e9ece8"/>
    </linearGradient>
    <linearGradient id="aboutFade" x1="0" y1="0" x2="1" y2="0">
      <stop offset="0" stop-color="#fff" stop-opacity="0"/><stop offset=".55" stop-color="#fff" stop-opacity=".2"/><stop offset="1" stop-color="#fff" stop-opacity=".95"/>
    </linearGradient>
  </defs>
  <rect x="150" y="0" width="86" height="387" rx="43" fill="url(#aboutFill)"/>
  <rect x="0" y="151" width="386" height="84" rx="42" fill="url(#aboutFill)"/>
  <rect x="0" y="0" width="558" height="387" fill="url(#aboutFade)"/>
</svg>
<div class="abs about-text">
  <h2>About Us</h2>
  <p>We are a dedicated team of licensed mental health professionals committed to supporting your emotional well-being. Whether you're facing anxiety, depression, trauma, relationship challenges, or simply need someone to talk to — we're here to help.</p>
  <p>Our practice is rooted in empathy, confidentiality, and personalized care, because every journey to mental wellness is unique.</p>
</div>
<a class="btn btn-orange" style="left:688px;top:983px;width:113px;height:30px;padding-left:16px">Learn More <span class="arrow-dot light" style="width:22px;height:22px"><svg><use href="#chev-r"/></svg></span></a>

<!-- Services -->
<section class="abs services">
  <h2 class="section-title" style="top:54px">Our Services</h2>
  <a class="nav-arrow" style="left:70px;top:234px"><svg><use href="#chev-l"/></svg></a>
  <a class="nav-arrow" style="left:1100px;top:234px"><svg><use href="#chev-r"/></svg></a>

  <article class="service-card" style="left:122px">
    <div class="photo" role="img" aria-label="Family of four talking with a counselor on a sofa" style="background:linear-gradient(135deg,#d9d6d1,#8d857b)"></div>
    <div class="foot"><h3>Couples &amp; Family<br>Counseling</h3><span class="arrow-dot"><svg><use href="#chev-r"/></svg></span></div>
  </article>
  <article class="service-card" style="left:366px">
    <div class="photo" role="img" aria-label="Therapist listening to a client in a calm office" style="background:linear-gradient(135deg,#c9c7c0,#6d5a6b)"></div>
    <div class="foot"><h3>Trauma-Informed<br>Care &amp; EMDR</h3><span class="arrow-dot"><svg><use href="#chev-r"/></svg></span></div>
  </article>
  <article class="service-card" style="left:610px">
    <div class="photo" role="img" aria-label="Young girl sitting with a counselor on a grey couch" style="background:linear-gradient(135deg,#bdbab5,#7b6f74)"></div>
    <div class="foot"><h3>Child &amp; Adolescent<br>Therapy</h3><span class="arrow-dot"><svg><use href="#chev-r"/></svg></span></div>
  </article>
  <article class="service-card" style="left:853px">
    <div class="photo" role="img" aria-label="Woman meditating at a desk against a pink wall" style="background:linear-gradient(135deg,#e8a0a4,#c4545d)"></div>
    <div class="foot"><h3>Stress &amp; Burnout<br>Management</h3><span class="arrow-dot"><svg><use href="#chev-r"/></svg></span></div>
  </article>

  <a class="btn btn-orange" style="left:529px;top:393px;width:141px;height:30px;padding-left:14px">View All Services <span class="arrow-dot light" style="width:22px;height:22px"><svg><use href="#chev-r"/></svg></span></a>
</section>

<!-- Why choose us -->
<h2 class="section-title" style="top:1689px">Why Choose Us</h2>
<a class="nav-arrow" style="left:70px;top:1819px"><svg><use href="#chev-l"/></svg></a>
<a class="nav-arrow" style="left:1100px;top:1819px"><svg><use href="#chev-r"/></svg></a>

<div class="why-card" style="left:122px">
  <span class="icon"><svg viewBox="0 0 36 36" fill="none" stroke="#fff" stroke-width="1.6"><circle cx="18" cy="11" r="6"/><path d="M7 32c0-7 5-11 11-11s11 4 11 11"/><path d="M14 23v5h8v-5"/></svg></span>
  <h3>Licensed and<br>Experienced Therapists</h3>
</div>
<div class="why-card" style="left:447px">
  <span class="icon"><svg viewBox="0 0 36 36" fill="none" stroke="#fff" stroke-width="1.6"><circle cx="13" cy="7" r="3.5"/><path d="M13 12v11M9 33l4-10 4 10M7 17l6-4 6 4"/><path d="M22 17l7 2v6c0 4-3 6-7 8-4-2-7-4-7-8" /><path d="M19 25l2 2 4-4"/></svg></span>
  <h3>Insurance Accepted</h3>
</div>
<div class="why-card" style="left:771px">
  <span class="icon"><svg viewBox="0 0 36 36" fill="none" stroke="#fff" stroke-width="1.6"><circle cx="20" cy="9" r="4"/><path d="M14 20l6-5 6 5"/><path d="M4 24h7l6 3h9c2 0 3-2 1-3l-7-2"/><path d="M4 30h6l8 2 12-6"/></svg></span>
  <h3>Holistic and Integrative<br>Treatment</h3>
</div>

<!-- Testimonials -->
<section class="abs testimonials" role="img" aria-label="Soft light blue background with a faint honeycomb texture"></section>
<h2 class="section-title" style="top:2009px">What Our Clients Say</h2>
<a class="nav-arrow" style="left:70px;top:2150px"><svg><use href="#chev-l"/></svg></a>
<a class="nav-arrow" style="left:1100px;top:2150px"><svg><use href="#chev-r"/></svg></a>

<div class="review" style="left:122px">
  <div class="avatar" role="img" aria-label="Portrait photo of the reviewer"></div>
  <div class="who">Nora P., Washington DC</div>
  <div class="stars"><svg><use href="#star"/></svg><svg><use href="#star"/></svg><svg><use href="#star"/></svg><svg><use href="#star"/></svg><svg><use href="#star"/></svg></div>
  <blockquote>“The therapists here are incredibly compassionate and skilled. I felt supported every step of the way”</blockquote>
</div>
<div class="abs review-divider"></div>
<div class="review" style="left:687px">
  <div class="avatar" role="img" aria-label="Portrait photo of the reviewer" style="background:linear-gradient(160deg,#e2c9a8,#7a6450)"></div>
  <div class="who">Elliot R., Bethesda</div>
  <div class="stars"><svg><use href="#star"/></svg><svg><use href="#star"/></svg><svg><use href="#star"/></svg><svg><use href="#star"/></svg><svg><use href="#star"/></svg></div>
  <blockquote>“They helped me reconnect with myself after years of struggling with anxiety. I’m finally hopeful again.”</blockquote>
</div>

<!-- Blog -->
<h2 class="section-title" style="top:2398px;font-weight:500">Mental Health Insights &amp; Resources</h2>
<a class="nav-arrow" style="left:68px;top:2604px"><svg><use href="#chev-l"/></svg></a>
<a class="nav-arrow" style="left:1102px;top:2604px"><svg><use href="#chev-r"/></svg></a>

<article class="post-card" style="left:122px;background:linear-gradient(135deg,#d9d4cd,#5d6c7d)" role="img" aria-label="Counselor comforting a worried young man">
  <div class="caption"><h3>Understanding the Signs<br>of Depression</h3><span class="arrow-dot"><svg><use href="#chev-r"/></svg></span></div>
</article>
<article class="post-card" style="left:447px;background:linear-gradient(135deg,#c8c6c2,#4a4a4c)" role="img" aria-label="Stressed person holding their head beside a clinician">
  <div class="caption"><h3>How Therapy Can Help<br>with Burnout</h3><span class="arrow-dot"><svg><use href="#chev-r"/></svg></span></div>
</article>
<article class="post-card" style="left:772px;background:linear-gradient(135deg,#e6e1d6,#8f8f6e)" role="img" aria-label="Woman meditating cross-legged in a bright kitchen">
  <div class="caption"><h3>Mindfulness Techniques for<br>Daily Life</h3><span class="arrow-dot"><svg><use href="#chev-r"/></svg></span></div>
</article>

<!-- CTA -->
<section class="abs cta">
  <h2>Ready to Take the First Step?</h2>
  <p>You don’t have to go through this alone. Let’s talk — your path to healing begins with a single conversation.</p>
  <a class="btn btn-white" style="left:518px;top:155px;width:152px;height:31px;padding-left:17px">Contact Us Today <span class="arrow-dot" style="width:22px;height:22px"><svg><use href="#chev-r"/></svg></span></a>
</section>

<!-- Footer -->
<footer class="abs site-footer">
  <div class="logo" style="left:122px;top:57px"><span class="name">Calder Health</span><span class="tag">SERVICES</span></div>
  <h4 style="left:122px;top:120px">Follow Us</h4>
  <a class="social" style="left:122px;top:147px" aria-label="Social profile 1"><span></span></a>
  <a class="social" style="left:156px;top:147px" aria-label="Social profile 2"><span></span></a>
  <a class="social" style="left:189px;top:147px" aria-label="Social profile 3"><span></span></a>
  <a class="social" style="left:221px;top:147px" aria-label="Social profile 4"><span></span></a>

  <h4 style="left:406px;top:60px">Quick Links</h4>
  <nav class="foot-links">
    <a style="left:406px;top:95px">Home</a>
    <a style="left:406px;top:122px">About Us</a>
    <a style="left:406px;top:149px">Services</a>
    <a style="left:406px;top:176px">Blog</a>
  </nav>

  <h4 style="left:615px;top:60px">Contact Info</h4>
  <div class="foot-contact">
    <div style="left:615px;top:88px"><span class="contact-ico"><svg viewBox="0 0 12 12" fill="none" stroke="#f58220" stroke-width="1.2"><path d="M2.5 1.5h2l1 2.5-1.2.8a6 6 0 003 3l.8-1.2 2.5 1v2c0 .5-.5 1-1 1A9 9 0 011.5 2.5c0-.5.5-1 1-1z"/></svg></span>+1 202-555-0148</div>
    <div style="left:615px;top:128px"><span class="contact-ico"><svg viewBox="0 0 12 12" fill="none" stroke="#f58220" stroke-width="1.2"><rect x="1.5" y="3" width="9" height="6.5" rx="1"/><path d="M1.5 3.5L6 7l4.5-3.5"/></svg></span>hello@calderhealth.example</div>
    <div style="left:615px;top:168px"><span class="contact-ico"><svg viewBox="0 0 12 12" fill="none" stroke="#f58220" stroke-width="1.2"><circle cx="6" cy="6" r="4.5"/><path d="M1.5 6h9M6 1.5c2 2.5 2 6.5 0 9M6 1.5c-2 2.5-2 6.5 0 9"/></svg></span>calderhealthservices.example</div>
  </div>

  <h4 style="left:862px;top:62px">Newsletter Signup</h4>
  <div class="email-field">Email</div>
  <a class="subscribe">SUBSCRIBE</a>

  <div class="foot-rule"></div>
  <div class="copyright">Copyright © 2025 <span style="font-size:11.5px">CalderHealthServices</span> All rights reserved.</div>
  <div class="legal"><a>Company</a><a>Privacy Policy</a><a>Terms and Conditions</a></div>
</footer>

</body>
</html>
```